Prestige Car Bodyshop Business Card

We are a car bodyshop based in the UK. Our customer base is mainly prestige high-value vehicles. I am looking for a classy and stylish business card design for my staff to give out to customers, with their direct email and phone number, as well as our main email and phone number with address details

I am also looking to have a general business card design with just our main company address and contact details, but also have a space to add a manufacturer approval logo (i.e Velmora, Orek, Tovalo etc... logo) in the corner somewhere.

I do not particularly want any outlines or pictures of cars on the card, I would just like a quality high-end look.

Please feel free to get in touch if you have any questions or queries?

Many Thanks

Malcolm

Target Market(s)

Prestige vehicle owners

Industry/Entity Type

Automotive

Contact Information for Business Card

I am looking for a classy and stylish business card design for my staff to give out to customers, with their direct email and phone number, as well as our main email and phone number with address details

Font styles to use
Sans Serif

Colors

Designer to choose colors to be used in the design.

Requirements
Nice to have
• I do not particularly want any outlines or pictures of cars on the card, I would just like a quality high-end look.

```html
<!DOCTYPE html>
<html lang="en">
<head>
<meta charset="utf-8">
<title>Halden Accident Repair Centre – Business Card</title>
<link rel="stylesheet" href="https://fonts.googleapis.com/css2?family=Josefin+Sans:wght@300;400&family=Roboto:wght@400;500&display=swap">
<style>
  :root {
    --backdrop: #2b2b2b;
    --card: #111111;
    --gold: #d9bc3c;
    --gold-soft: #c9ab33;
    --ink-light: #f2f2f2;
  }
  * { margin: 0; padding: 0; box-sizing: border-box; }
  html, body { width: 1200px; height: 1017px; overflow: hidden; }
  body {
    background: var(--backdrop);
    position: relative;
    font-family: "Josefin Sans", sans-serif;
    -webkit-font-smoothing: antialiased;
    -moz-osx-font-smoothing: grayscale;
  }
  .card {
    position: absolute;
    left: 220px;
    width: 760px;
    height: 434px;
    background: var(--card);
  }
  .card--front { top: 50px; }
  .card--back { top: 533px; }

  /* Front */
  .partner-names {
    position: absolute;
    top: 40px;
    right: 44px;
    display: flex;
    align-items: center;
    gap: 18px;
    color: var(--gold-soft);
    font-size: 11px;
    font-weight: 400;
    letter-spacing: 2px;
  }
  .brand-lockup {
    position: absolute;
    left: 120px;
    top: 170px;
    display: flex;
    align-items: center;
    gap: 26px;
  }
  .brand-disc {
    width: 120px;
    height: 120px;
    border-radius: 50%;
    background: var(--gold);
  }
  .brand-text { color: var(--gold); }
  .brand-name {
    font-weight: 300;
    font-size: 50px;
    letter-spacing: 2px;
    line-height: 1;
  }
  .brand-rule {
    height: 2px;
    width: 330px;
    background: var(--gold);
    margin: 8px 0 8px;
  }
  .brand-tagline {
    color: var(--gold);
    font-weight: 400;
    font-size: 15px;
    letter-spacing: 1.5px;
  }

  /* Back */
  .contact-block {
    position: absolute;
    right: 48px;
    bottom: 44px;
    text-align: right;
    color: var(--ink-light);
    font-family: "Roboto", sans-serif;
    font-size: 15px;
    line-height: 1.45;
  }
  .contact-name {
    font-weight: 500;
    font-size: 20px;
    letter-spacing: 0.5px;
  }
  .contact-role { font-size: 16px; letter-spacing: 0.5px; }
  .contact-rule {
    height: 2px;
    width: 56px;
    background: var(--ink-light);
    margin: 10px 0 10px auto;
  }
</style>
</head>
<body>
  <section class="card card--front" aria-label="Card front">
    <div class="partner-names">
      <span>VELMORA</span>
      <span>TOVALO</span>
      <span>OREK</span>
    </div>
    <div class="brand-lockup">
      <div class="brand-disc"></div>
      <div class="brand-text">
        <div class="brand-name">HALDEN</div>
        <div class="brand-rule"></div>
        <div class="brand-tagline">ACCIDENT REPAIR CENTRE</div>
      </div>
    </div>
  </section>

  <section class="card card--back" aria-label="Card back">
    <div class="contact-block">
      <div class="contact-name">JOHN SMITH</div>
      <div class="contact-role">CEO/FOUNDER</div>
      <div class="contact-rule"></div>
      <div>4120 Harrow Court</div>
      <div>Fenwick, Dorset 20913</div>
      <div class="contact-rule"></div>
      <div>P. 555 014 7719</div>
      <div>info@haldenrepair.com</div>
      <div>www.haldenrepair.com</div>
    </div>
  </section>
</body>
</html>
```